Varnel Psychiatry (Psychiatry clinic offering cutting edge treatments)

2 sided flyer for new psychiatry practice in Boulder, CO. I want something that looks professional, cutting edge, but also welcoming and friendly. My logo and pictures are attached.

Some of the copy:
Personalized, holistic Psychiatry combined with cutting-edge, evidence-based treatments. Our personalized psychiatry plan includes a bio-psycho-social evaluation, personalized treatment plan, medical evaluation for underlying hormonal and electrolyte abnormalities, and genetic testing (when warranted).

We specialize in treatment-resistant depression and substance abuse. We also treat PTSD, Bipolar Disorder, OCD, anxiety disorders, ADHD, and psychotic disorders.

About Dr. Brok- Dr. Brok served as Chief Resident at the largest private psychiatry hospital in Colorado. While there he won 3 consecutive awards for exceptionally high Psychiatry in service test score (99th percentile). He was a board member of Kestrel Mind Guild and helped advocate for better Colorado mental health policy. Dr. Brok is uniquely trained in Ketamine, Transcranial Magnetic Stimulation, and integrative psychiatry.

Target Market(s)

Private pay mental health patients, planning to give out to psychologists and family practice doctors

Industry/Entity Type

Medicine/Psychiatry

Colors
0054AA
0677BA
7BADD7
CADEEF
E8F1F8
0094D4
00A9DD
6FCCEA
C7EBF8
E9F6FB
00AB8E
00BBA5
67D7C9
C6EFE9
E9F9F6

Requirements
Must have
• My logo, an about me (Dr. Tomas Brok) section

```html
<!DOCTYPE html>
<html lang="en">
<head>
<meta charset="utf-8">
<title>Varnel Psychiatry – Two-Sided Flyer</title>
<link href="https://fonts.googleapis.com/css2?family=Mulish:wght@400;600;700;800&display=swap" rel="stylesheet">
<style>
  :root{
    --navy:#0054AA;
    --deep:#0a47b0;
    --ink:#1b1b24;
    --pale:#CADEEF;
    --paler:#d6e5f5;
    --mid:#7BADD7;
    --sky:#0094D4;
    --aqua:#6FCCEA;
    --mint:#67D7C9;
    --stage:#3f7fc6;
    --white:#ffffff;
  }
  *{box-sizing:border-box;margin:0;padding:0}
  html,body{width:1200px;height:800px;overflow:hidden}
  body{background:var(--stage);font-family:"Mulish",sans-serif;color:var(--ink);position:relative}
  .page{position:absolute;top:20px;width:544px;height:760px;overflow:hidden;background:var(--paler)}
  .page--front{left:36px}
  .page--back{left:620px}
  .abs{position:absolute}

  /* front */
  .hero{left:0;top:0}
  .brand{left:22px;top:22px;display:flex;align-items:center;gap:8px;
    font-weight:800;font-size:22px;letter-spacing:1px;color:var(--navy)}
  .brand__dot{width:26px;height:26px;border-radius:50%;background:var(--navy)}
  .headline{left:0;width:544px;top:370px;text-align:center;font-weight:800;font-size:18px;line-height:1.35}
  .headline__blue{color:var(--navy)}
  .circle{border-radius:50%}
  .circle--blue{left:106px;top:462px;width:134px;height:134px;background:radial-gradient(circle at 45% 40%,#3a7fd8,#0a3fa6)}
  .circle--photo{left:18px;top:436px;width:150px;height:150px;border:4px solid var(--paler);
    background:linear-gradient(135deg,#d9c7ad,#b58f62 60%,#6e7fa0)}
  .specialties{left:262px;top:436px;width:268px;font-size:13px;line-height:1.36}
  .approach{left:22px;top:634px;width:506px;font-size:12.8px;line-height:1.36}
  .footer-shapes{left:0;bottom:0}

  /* back */
  .copy{font-size:10.4px;line-height:1.5;text-align:justify;color:var(--ink)}
  .rootcauses{left:18px;top:22px;width:270px}
  .photo--thinker{left:304px;top:22px;width:238px;height:182px;background:linear-gradient(160deg,#d7d0ba,#a9a48f 55%,#6c6a5e)}
  .photo--blur{left:0;top:226px;width:234px;height:200px;background:radial-gradient(ellipse at 50% 45%,#8e8e96,#2d2d33 55%,#050507)}
  .plan{left:254px;top:244px;width:272px}
  .about{left:0;top:452px;width:544px;height:308px;background:var(--deep)}
  .about__title{left:20px;top:24px;color:var(--white);font-weight:800;font-size:16px}
  .about__text{left:20px;top:52px;width:270px;color:var(--white)}
  .photo--doctor{left:306px;top:14px;width:238px;height:294px;
    background:radial-gradient(ellipse at 55% 40%,#d8d8d8,#8a8a8a 55%,#1d1d1d)}
</style>
</head>
<body>

<section class="page page--front">
  <svg class="abs hero" width="544" height="360" viewBox="0 0 544 360">
    <defs>
      <linearGradient id="heroFill" x1="0" y1="0" x2="1" y2="1">
        <stop offset="0" stop-color="#e9e6e0"/>
        <stop offset=".55" stop-color="#a9aeb8"/>
        <stop offset="1" stop-color="#3c4656"/>
      </linearGradient>
    </defs>
    <path d="M0 225 C60 290 165 326 290 326 C420 326 515 285 544 200 V250 C505 318 420 346 290 348 C165 350 55 310 0 258 Z" fill="var(--navy)"/>
    <path d="M470 290 C500 275 525 250 544 215 V240 C522 275 500 292 470 302 Z" fill="var(--sky)" opacity=".8"/>
    <path role="img" aria-label="Photo: young patient talking with a therapist on a blue sofa"
      d="M0 0 H544 V190 C520 265 420 302 290 304 C165 306 60 272 0 215 Z" fill="url(#heroFill)"/>
  </svg>
  <div class="abs brand"><span class="brand__dot"></span>Varnel Psychiatry</div>

  <h1 class="abs headline"><span class="headline__blue">Varnel Psychiatry is now accepting new</span><br>patients in Boulder, Colorado!</h1>

  <div class="abs circle circle--blue" role="img" aria-label="Photo: distressed woman in blue tone"></div>
  <div class="abs circle circle--photo" role="img" aria-label="Photo: smiling couple in a counseling session"></div>

  <p class="abs specialties">We specialize in treating patients with treatment resistant depression and substance abuse disorders who have not responded to other forms of treatment. We also treat patients with PTSD, Bipolar Disorder, OCD, anxiety disorders, ADHD, and psychotic disorders. We believe that by providing comprehensive care, we can help our patients heal both emotionally and physically.</p>

  <p class="abs approach">We know that mental health is complex and that multiple factors can contribute to the development of mental illness. For this reason, we take an integrative approach that considers the whole person. We understand that each individual has their own unique set of experiences, strengths, and challenges, and we tailor our treatment plans to suit each patient’s personal needs.</p>

  <svg class="abs footer-shapes" width="544" height="50" viewBox="0 0 544 50">
    <path d="M0 28 L26 50 H0 Z" fill="var(--aqua)" opacity=".7"/>
    <path d="M20 50 L60 34 L100 50 Z" fill="var(--mint)" opacity=".55"/>
    <path d="M80 50 L140 26 L200 50 Z" fill="var(--mint)" opacity=".45"/>
    <path d="M160 50 L190 38 L225 50 Z" fill="var(--aqua)" opacity=".6"/>
    <path d="M300 50 L360 24 L420 50 Z" fill="var(--aqua)" opacity=".7"/>
    <path d="M0 50 L40 42 L70 50 Z" fill="#1b2f6e"/>
    <path d="M410 50 L544 10 V50 Z" fill="#1b2f6e"/>
  </svg>
</section>

<section class="page page--back">
  <p class="abs copy rootcauses">So often, when we think about mental health, we focus on just treating symptoms. If someone is depressed, they might take medication to help them feel better. If someone is anxious, they might see a therapist to help them manage their anxiety. While these treatments can be helpful, they only address the symptoms of mental illness. To truly address mental health, it is necessary to treat the root causes. This might involve addressing childhood trauma, unresolved conflict, or feelings of worthlessness. It might also involve developing healthy coping mechanisms and learning how to set boundaries. By treating the root causes of mental illness, we can begin to create lasting change.</p>
  <div class="abs photo--thinker" role="img" aria-label="Photo: young man sitting on the floor beneath tangled scribbled lines"></div>

  <div class="abs photo--blur" role="img" aria-label="Photo: motion-blurred figure on black background"></div>
  <p class="abs copy plan">Our personalized psychiatry plan includes a bio-psycho-social evaluation, tailored treatment plan, medical evaluation for underlying hormonal and electrolyte abnormalities, and genetic testing (when warranted). Our integrative psychiatry approach combines cutting edge, evidence-based treatments with holistic therapies to provide you with the best possible care. In addition, we also offer Ketamine Assisted Therapy, TMS (Transcranial Magnetic Simulation), and MAT Treatment for Substance abuse. We pride ourselves on always staying up to date on the latest mental health treatments.</p>

  <div class="abs about">
    <h2 class="abs about__title">ABOUT ME</h2>
    <p class="abs copy about__text">Dr. Tomas Brok is a psychiatrist with years of experience providing compassionate, evidence-based care to patients of all ages. He is uniquely trained in several cutting-edge treatments, including Ketamine, Transcranial Magnetic Stimulation (TMS), and integrative psychiatry. Prior to founding Varnel Psychiatry, Dr. Brok served as Chief Resident at the largest private psychiatry hospital in Colorado. While there, he won three consecutive awards for exceptionally high Psychiatry in-service test scores (99th percentile). In addition, he was a board member of the Kestrel Mind Guild and helped advocate for better Colorado mental health policy. Thanks to his extensive training and experience, Dr. Brok is able to provide each patient with an individualized treatment plan that brings optimum results.</p>
    <div class="abs photo--doctor" role="img" aria-label="Black and white portrait photo of Dr. Tomas Brok"></div>
  </div>
</section>

</body>
</html>
```